Velmora Business Card

We need a design for business cards for our new company. We are a resident safety and security company company that focuses on senior living communities. we provide Nurse call, Access control, CCTV, Wired and wireless network infrastructure, Wander Management, and much more!

Our logo is the circuit board shield. Representing our high tech security solutions. I would like the business card to bring the same theme with perhaps some circuit board traces around the card similar to our logo

```html
<!DOCTYPE html>
<html lang="en">
<head>
<meta charset="utf-8">
<title>Velmora Business Card</title>
<link href="https://fonts.googleapis.com/css2?family=Cinzel:wght@500;700&family=Montserrat:wght@400;500;700&display=swap" rel="stylesheet">
<style>
  :root{
    --stage-top:#d4d4d4;
    --stage-bottom:#a9a9a9;
    --brand-blue:#2a55b0;
    --deep-blue:#2c58ad;
    --mid-blue:#2f7ccc;
    --sky-blue:#37b4e8;
    --white:#ffffff;
    --soft-white:#eaf3ff;
  }
  *{box-sizing:border-box;margin:0;padding:0}
  html,body{width:1200px;height:802px;overflow:hidden}
  body{
    background:linear-gradient(180deg,var(--stage-top),var(--stage-bottom));
    font-family:"Montserrat",sans-serif;
    position:relative;
  }
  .card{
    position:absolute;
    top:246px;
    width:540px;height:309px;
    border-radius:20px;
    overflow:hidden;
    box-shadow:0 18px 36px rgba(0,0,0,.28);
  }
  .card--front{left:40px;background:var(--white)}
  .card--back{left:620px}
  .card-art{position:absolute;inset:0;width:100%;height:100%}

  /* front */
  .wordmark{
    position:absolute;left:30px;top:70px;
    font-family:"Cinzel",serif;font-weight:700;font-size:40px;
    color:var(--brand-blue);letter-spacing:1px;
  }
  .brand-spot{
    position:absolute;right:34px;top:60px;
    display:flex;align-items:center;gap:8px;
    font-family:"Cinzel",serif;font-weight:700;font-size:18px;color:var(--white);
  }
  .brand-dot{width:22px;height:22px;border-radius:50%;background:var(--white)}
  .person{position:absolute;left:40px;top:162px;color:var(--white)}
  .person-name{font-family:"Cinzel",serif;font-weight:700;font-size:18px;letter-spacing:.5px}
  .person-role{font-size:12px;font-weight:500;margin-top:1px}
  .person-rule{width:18px;height:1px;background:var(--white);margin:8px 0 7px}
  .contact-list{list-style:none}
  .contact-list li{display:flex;align-items:center;gap:8px;font-size:12px;line-height:18px}
  .contact-list svg{width:11px;height:11px;fill:var(--white);flex:none}

  /* back */
  .back-brand{
    position:absolute;left:0;right:0;top:92px;
    display:flex;justify-content:center;align-items:center;gap:12px;
    font-family:"Cinzel",serif;font-weight:700;font-size:38px;color:var(--white);letter-spacing:1px;
  }
  .back-brand .brand-dot{width:30px;height:30px}
  .services-heading{
    position:absolute;left:36px;right:36px;top:168px;
    display:flex;align-items:center;gap:12px;
    font-weight:700;font-size:15px;color:var(--white);letter-spacing:.5px;white-space:nowrap;
  }
  .services-heading::before,.services-heading::after{content:"";flex:1;height:1px;background:var(--soft-white)}
  .services-list{
    position:absolute;left:30px;right:30px;top:204px;
    text-align:center;color:var(--white);font-size:13.5px;font-weight:500;line-height:26px;
  }
</style>
</head>
<body>

<section class="card card--front" aria-label="Business card front">
  <svg class="card-art" viewBox="0 0 540 309" preserveAspectRatio="none" aria-hidden="true">
    <defs>
      <linearGradient id="frontBlue" x1="0" y1="1" x2="1" y2="0">
        <stop offset="0" stop-color="#2c58ad"/>
        <stop offset=".6" stop-color="#2f7ccc"/>
        <stop offset="1" stop-color="#37b4e8"/>
      </linearGradient>
    </defs>
    <path d="M0,150 C160,140 340,95 540,0 L540,309 L0,309 Z" fill="#37b4e8"/>
    <path d="M0,168 C170,150 350,100 540,14 L540,309 L0,309 Z" fill="url(#frontBlue)"/>
    <path d="M0,168 C170,150 350,100 540,14" fill="none" stroke="#8fd6f5" stroke-width="2"/>
  </svg>

  <div class="wordmark">VELMORA</div>
  <div class="brand-spot"><span class="brand-dot"></span>Velmora</div>

  <div class="person">
    <div class="person-name">MARA LINDQVIST</div>
    <div class="person-role">President</div>
    <div class="person-rule"></div>
    <ul class="contact-list">
      <li><svg viewBox="0 0 24 24"><path d="M6.6 10.8a15 15 0 0 0 6.6 6.6l2.2-2.2a1 1 0 0 1 1-.25 11.4 11.4 0 0 0 3.6.57 1 1 0 0 1 1 1V20a1 1 0 0 1-1 1A17 17 0 0 1 3 4a1 1 0 0 1 1-1h3.5a1 1 0 0 1 1 1 11.4 11.4 0 0 0 .57 3.6 1 1 0 0 1-.25 1z"/></svg>(555) 014-2290</li>
      <li><svg viewBox="0 0 24 24"><path d="M7 1h10a2 2 0 0 1 2 2v18a2 2 0 0 1-2 2H7a2 2 0 0 1-2-2V3a2 2 0 0 1 2-2zm0 3v14h10V4z"/></svg>(555) 017-4438</li>
      <li><svg viewBox="0 0 24 24"><path d="M2 5h20v14H2zm2 2v.5l8 5 8-5V7l-8 5z"/></svg>Mara@Velmora.com</li>
      <li><svg viewBox="0 0 24 24"><path d="M12 2a10 10 0 1 0 0 20 10 10 0 0 0 0-20zm0 2c1 1.3 1.8 3 2.1 5H9.9C10.2 7 11 5.3 12 4zM4.3 11h3.6a16 16 0 0 0 0 2H4.3a8 8 0 0 1 0-2zm5.6 0h4.2a14 14 0 0 1 0 2H9.9a14 14 0 0 1 0-2zm6.2 0h3.6a8 8 0 0 1 0 2h-3.6a16 16 0 0 0 0-2zM9.9 15h4.2c-.3 2-1.1 3.7-2.1 5-1-1.3-1.8-3-2.1-5z"/></svg>www.Velmora.com</li>
    </ul>
  </div>
</section>

<section class="card card--back" aria-label="Business card back">
  <svg class="card-art" viewBox="0 0 540 309" preserveAspectRatio="none" role="img" aria-label="Faint circuit board trace pattern over blue gradient">
    <defs>
      <linearGradient id="backBlue" x1="0" y1="1" x2="1" y2="0">
        <stop offset="0" stop-color="#37b4e8"/>
        <stop offset=".5" stop-color="#2f7ccc"/>
        <stop offset="1" stop-color="#2c58ad"/>
      </linearGradient>
    </defs>
    <rect width="540" height="309" fill="url(#backBlue)"/>
  </svg>

  <div class="back-brand"><span class="brand-dot"></span>VELMORA</div>
  <h2 class="services-heading">OUR SERVICES</h2>
  <p class="services-list">
    • Nurse call &nbsp;• Access control &nbsp;• CCTV &nbsp;• Wander Management<br>
    • Wired and wireless network infrastructure &nbsp;• and much more!
  </p>
</section>

</body>
</html>
```